BEACH CLUB OPENING INVITATION & FLYER DESIGN

Hi! I need a posh opening poster design for a new upscale beach club we are opening in Bodrum/Turkey. The text should be in english and turkish. Written text on the invitation and flyer should be:
Title: GRAND OPENING PARTY (Only written in English)
Date & Time: 28.05.2016 - 21:00
Address: Yalıkavak Mahallesi Menekşe Sokak No: 5, Bodrum, Muğla / Türkiye
Website: www.lorvanbeachclub.com
Email: info@lorvanbeachclub.com
Tel: +90 (252) 764 18 27
Follow Us / Bizi Takip Edin
Instagram: /lorvanbeachclub
Facebook: /lorvanbeachclub
P.S: I attached the logo and some sample posters
Best of Luck

```html
<!DOCTYPE html>
<html lang="en">
<head>
<meta charset="utf-8">
<title>Lorvan Beach Club – Grand Opening Party</title>
<link rel="stylesheet" href="https://fonts.googleapis.com/css2?family=Oswald:wght@400;500&family=Righteous&display=swap">
<style>
  :root {
    --page: #5a5a5a;
    --ink: #0b0b0b;
    --gold: #e2bb22;
    --gold-light: #f7e27a;
    --gold-dark: #a9840e;
    --silver: #e8e8e8;
    --silver-dark: #9c9c9c;
    --text-light: #f2f2f2;
    --text-dim: #cfcfcf;
    --footer-ink: #1a1a1a;
  }
  * { box-sizing: border-box; margin: 0; padding: 0; }
  html, body { width: 1200px; height: 812px; overflow: hidden; background: var(--page); }

  .sheet {
    position: absolute; overflow: hidden;
    background:
      radial-gradient(ellipse 45% 25% at 35% 12%, rgba(255,255,255,.45), transparent 70%),
      linear-gradient(120deg, #1c1c1c 0%, #3a3a3a 30%, #151515 55%, #2b2b2b 75%, var(--ink) 100%);
    box-shadow: 0 6px 18px rgba(0,0,0,.5);
    font-family: "Oswald", sans-serif;
  }
  .sheet--poster { left: 108px; top: 26px; width: 535px; height: 757px; }
  .sheet--flyer { left: 743px; top: 155px; width: 333px; height: 501px; }

  .photo {
    position: absolute; left: 0; top: 0;
    background:
      radial-gradient(ellipse 32% 18% at 42% 14%, #f4f4f4, rgba(244,244,244,0) 75%),
      radial-gradient(ellipse 22% 14% at 45% 22%, #9a9a9a, transparent 80%),
      radial-gradient(ellipse 40% 20% at 30% 50%, #d8d8d8, transparent 80%),
      radial-gradient(ellipse 75% 32% at 35% 82%, #ffffff, rgba(255,255,255,0) 80%),
      linear-gradient(90deg, #cfcfcf 0%, #9d9d9d 55%, #3a3a3a 100%);
    -webkit-mask-image: linear-gradient(90deg, #000 62%, transparent 100%);
    mask-image: linear-gradient(90deg, #000 62%, transparent 100%);
  }
  .sheet--poster .photo { width: 420px; height: 692px; }
  .sheet--flyer .photo { width: 250px; height: 455px; }

  .line {
    position: absolute; display: block; white-space: nowrap; text-align: center; line-height: 1;
  }
  .headline { font-family: "Righteous", sans-serif; letter-spacing: 1px; }
  .headline--gold {
    color: var(--gold);
    background: linear-gradient(180deg, var(--gold-light), var(--gold) 55%, var(--gold-dark));
    -webkit-background-clip: text; background-clip: text; -webkit-text-fill-color: transparent;
  }
  .headline--silver {
    color: var(--silver);
    background: linear-gradient(180deg, #fff, var(--silver) 50%, var(--silver-dark));
    -webkit-background-clip: text; background-clip: text; -webkit-text-fill-color: transparent;
  }
  .event-date { color: var(--text-dim); font-weight: 400; }
  .address { color: var(--text-light); font-weight: 500; }
  .website { color: var(--gold); font-weight: 500; }
  .brand__name { color: var(--gold); font-weight: 500; letter-spacing: 2px; }
  .brand__mark { position: absolute; border-radius: 50%; background: var(--gold); }
  .divider { position: absolute; height: 1px; background: linear-gradient(90deg, transparent, #c9a21c 20%, #e2bb22 50%, #c9a21c 80%, transparent); }

  /* Poster */
  .sheet--poster .line { left: 245px; width: 262px; }
  .sheet--poster .headline--grand { top: 26px; font-size: 77px; }
  .sheet--poster .headline--opening { top: 101px; font-size: 59px; }
  .sheet--poster .headline--party { top: 167px; font-size: 81px; }
  .sheet--poster .divider--top { left: 276px; width: 226px; top: 277px; }
  .sheet--poster .event-date--en { top: 312px; font-size: 28px; }
  .sheet--poster .event-date--tr { top: 353px; font-size: 28px; }
  .sheet--poster .divider--bottom { left: 276px; width: 226px; top: 407px; }
  .sheet--poster .address { top: 437px; font-size: 13.8px; line-height: 22px; }
  .sheet--poster .website { top: 491px; font-size: 24px; }
  .sheet--poster .brand__mark { left: 384px; top: 560px; width: 40px; height: 40px; }
  .sheet--poster .brand__name { left: 294px; width: 220px; top: 622px; font-size: 22px; }

  /* Flyer */
  .sheet--flyer .line { left: 178px; width: 138px; }
  .sheet--flyer .headline--grand { top: 19px; font-size: 40px; }
  .sheet--flyer .headline--opening { top: 57px; font-size: 30.5px; }
  .sheet--flyer .headline--party { top: 92px; font-size: 42px; }
  .sheet--flyer .divider--top { left: 217px; width: 81px; top: 147px; }
  .sheet--flyer .event-date--en { top: 164px; font-size: 14.5px; }
  .sheet--flyer .event-date--tr { top: 185px; font-size: 14.5px; }
  .sheet--flyer .divider--bottom { left: 217px; width: 81px; top: 214px; }
  .sheet--flyer .address { top: 230px; font-size: 7.2px; line-height: 11px; }
  .sheet--flyer .website { top: 258px; font-size: 12.5px; }
  .sheet--flyer .brand__mark { left: 245px; top: 292px; width: 20px; height: 20px; }
  .sheet--flyer .brand__name { left: 195px; width: 120px; top: 326px; font-size: 11px; letter-spacing: 1px; }
  .member-card {
    position: absolute; left: 185px; top: 370px; width: 127px; height: 80px; border-radius: 6px;
    background: linear-gradient(135deg, #f4f6f8 0%, #c9ccd1 45%, #e9ebee 70%, #aeb2b8 100%);
    box-shadow: 0 2px 5px rgba(0,0,0,.5);
  }

  /* Footer bands */
  .footer-band {
    position: absolute; left: 0; width: 100%;
    background: linear-gradient(180deg, var(--gold-light), var(--gold) 50%, var(--gold-dark));
    color: var(--footer-ink); white-space: nowrap;
  }
  .footer-band__item { position: absolute; top: 50%; transform: translateY(-50%); display: flex; align-items: center; gap: 5px; line-height: 1; }
  .social-square { background: var(--footer-ink); border-radius: 2px; flex: none; }
  .silver-band { position: absolute; left: 0; width: 100%; background: linear-gradient(180deg, #fdfdfd, #cfcfcf 60%, #a8a8a8); }

  .sheet--poster .footer-band { top: 692px; height: 41px; font-size: 12px; }
  .sheet--poster .silver-band { top: 735px; height: 22px; }
  .sheet--poster .footer-band__item--call { left: 16px; }
  .sheet--poster .footer-band__item--email { left: 154px; }
  .sheet--poster .footer-band__item--instagram { left: 329px; }
  .sheet--poster .footer-band__item--facebook { left: 426px; }
  .sheet--poster .social-square { width: 11px; height: 11px; }

  .sheet--flyer .footer-band { top: 455px; height: 19px; font-size: 6px; }
  .sheet--flyer .silver-band { top: 476px; height: 25px; }
  .sheet--flyer .footer-band__item { gap: 3px; }
  .sheet--flyer .footer-band__item--call { left: 19px; }
  .sheet--flyer .footer-band__item--email { left: 103px; }
  .sheet--flyer .footer-band__item--instagram { left: 210px; }
  .sheet--flyer .footer-band__item--facebook { left: 268px; }
  .sheet--flyer .social-square { width: 6px; height: 6px; border-radius: 1px; }
</style>
</head>
<body>
  <main class="sheet sheet--poster">
    <div class="photo" role="img" aria-label="Black and white photograph of a woman in a strapless white gown against a light burst"></div>

    <h1>
      <span class="line headline headline--gold headline--grand">GRAND</span>
      <span class="line headline headline--gold headline--opening">OPENING</span>
      <span class="line headline headline--silver headline--party">PARTY</span>
    </h1>
    <span class="divider divider--top" aria-hidden="true"></span>
    <p class="line event-date event-date--en">28 MAY 2016 - 21:00</p>
    <p class="line event-date event-date--tr">28 MAYIS 2016 - 21:00</p>
    <span class="divider divider--bottom" aria-hidden="true"></span>
    <p class="line address">YALIKAVAK MAHALLESI MENEKŞE<br>SOKAK NO: 5, BODRUM, MUĞLA / TÜRKIYE</p>
    <p class="line website">www.lorvanbeachclub.com</p>
    <span class="brand__mark" aria-hidden="true"></span>
    <p class="line brand__name">LORVAN BEACH CLUB</p>

    <footer class="footer-band">
      <span class="footer-band__item footer-band__item--call">CALL: +90 (252) 764 18 27</span>
      <span class="footer-band__item footer-band__item--email">Email: info@lorvanbeachclub.com</span>
      <span class="footer-band__item footer-band__item--instagram"><span class="social-square" aria-hidden="true"></span>/lorvanbeachclub</span>
      <span class="footer-band__item footer-band__item--facebook"><span class="social-square" aria-hidden="true"></span>/lorvanbeachclub</span>
    </footer>
    <div class="silver-band" aria-hidden="true"></div>
  </main>

  <aside class="sheet sheet--flyer">
    <div class="photo" role="img" aria-label="Black and white photograph of a woman in a strapless white gown against a light burst"></div>

    <h2>
      <span class="line headline headline--gold headline--grand">GRAND</span>
      <span class="line headline headline--gold headline--opening">OPENING</span>
      <span class="line headline headline--silver headline--party">PARTY</span>
    </h2>
    <span class="divider divider--top" aria-hidden="true"></span>
    <p class="line event-date event-date--en">28 MAY 2016 - 21:00</p>
    <p class="line event-date event-date--tr">28 MAYIS 2016 - 21:00</p>
    <span class="divider divider--bottom" aria-hidden="true"></span>
    <p class="line address">YALIKAVAK MAHALLESI MENEKŞE<br>SOKAK NO: 5, BODRUM, MUĞLA / TÜRKIYE</p>
    <p class="line website">www.lorvanbeachclub.com</p>
    <span class="brand__mark" aria-hidden="true"></span>
    <p class="line brand__name">LORVAN BEACH CLUB</p>
    <div class="member-card" role="img" aria-label="Silver platinum membership card"></div>

    <footer class="footer-band">
      <span class="footer-band__item footer-band__item--call">CALL: +90 (252) 764 18 27</span>
      <span class="footer-band__item footer-band__item--email">Email: info@lorvanbeachclub.com</span>
      <span class="footer-band__item footer-band__item--instagram"><span class="social-square" aria-hidden="true"></span>/lorvanbeachclub</span>
      <span class="footer-band__item footer-band__item--facebook"><span class="social-square" aria-hidden="true"></span>/lorvanbeachclub</span>
    </footer>
    <div class="silver-band" aria-hidden="true"></div>
  </aside>
</body>
</html>
```